Pharmacy and Travel Clinic Leaflet

We are an established pharmacy and gift shop which also runs a travel and vaccination clinic. We have had the same leaflet for a couple of years and would like to refresh it for the following reasons:
We have rebranded our travel and vaccination clinic as Fellgate Journey Clinic with its own dedicated website (www.fellgatejourneyclinic.co.uk).
We have made changes to our prices that need to be reflected in the new leaflet.

The original leaflet was a little information heavy as the service was new and we would like the new leaflet to be more visually appealing with the pharmacy side highlighting our services and using the colours of our logo (purple and green) and the vaccination side using the colours of our travel clinic logo (navy blue, light blue, red and white). Logo's are attached in a variety of formats as I have no idea what is most useful.

I will upload some images that may assist with the design, as well as updated text for the pharmacy leaflet and the new prices and text required for the vaccination side. I do not expect all of the images to be used.

The leaflet is to be two-sided, which we will print in A3 and possibly enlarge to use on a large A-Board.

I would like to receive the files in format(s) that can be sent to a printers and also added to our website to display our prices.

I have attached a copy of our existing leaflet for reference.

If any information requires clarification or there are files that you need to improve the design then please let me know and I will try to sort that out.

P.S. The font we usually use now is Orkney

I have an extra requirement if this is possible. On the pharmacy services side of the leaflet I would like the tagline Providing QRS services at the bottom right of the leaflet. It can go on the bottom left if necessary. It doesn't need to be large. It needs to be in the black font (Arial or Helvetica) with the QRS logo in blue. I have attached a link to the QRS logo website and files are now uploaded to give you an idea of what we need.
The Providing QRS services and logo need to be exactly as shown in the uploads. The QRS do not allow their logo to be used creatively.
https://www.example-qrs-health.org/qrsidentity/identity-guidelines/service-branding/

Thanks for all the submissions. They were very good but I had to choose one.

Target Market(s)

All ages from young students through to pensioners.

Industry/Entity Type

Pharmacy

Font styles to use
Sans Serif

Colors
9bcb3c
6c459b
ec1f27
0255a3
ffffff

Requirements
Must have
• Leaflet needs to be professional yet still be bold enough to stand out.
• Premium look using colours stated in brief. Colours differ for pharmacy side and travel clinic side. Please don't mix pharmacy and travel colours
Nice to have
• Please use the logos and tie the scheme in with those colours. Where the prices of vaccines are listed they need to be clear
• The Providing QRS services line and logo need to be exactly as shown in the uploads. The QRS do not allow their logo to be used creatively.
Should not have
• Must not be too informal. No comedy fonts

```html
<!DOCTYPE html>
<html lang="en">
<head>
<meta charset="utf-8">
<title>Birchwell Chemist &amp; Fellgate Journey Clinic Leaflet</title>
<link rel="stylesheet" href="https://fonts.googleapis.com/css2?family=Montserrat:wght@400;500;600;700;800&display=swap">
<style>
  :root {
    --purple: #6c459b;
    --green: #9bcb3c;
    --navy: #0255a3;
    --sky: #5bbdee;
    --red: #ec1f27;
    --white: #ffffff;
    --backdrop: #e9e9ec;
  }
  * { box-sizing: border-box; margin: 0; padding: 0; }
  html, body { width: 1200px; height: 776px; overflow: hidden; }
  body {
    background: var(--backdrop);
    font-family: "Montserrat", Arial, sans-serif;
    position: relative;
  }
  .leaflet {
    position: absolute;
    top: 38px;
    width: 495px;
    height: 700px;
    overflow: hidden;
    box-shadow: 0 6px 20px rgba(0,0,0,.18);
  }
  .leaflet svg.deco { position: absolute; left: 0; top: 0; }

  /* ---------- Pharmacy side ---------- */
  .pharmacy { left: 70px; background: var(--white); color: var(--purple); }
  .pharmacy .brand {
    position: absolute; top: 26px; left: 0; right: 0;
    display: flex; align-items: center; justify-content: center; gap: 10px;
    font-weight: 600; font-size: 20px; letter-spacing: .5px; text-transform: uppercase;
    color: var(--purple);
  }
  .pharmacy .brand-mark { width: 22px; height: 22px; background: var(--purple); }
  .pharmacy .intro {
    position: absolute; top: 82px; left: 50px; right: 16px;
    text-align: center; font-weight: 800; font-size: 11.5px; line-height: 1.6;
    letter-spacing: .2px; text-transform: uppercase; white-space: nowrap;
  }
  .services {
    position: absolute; top: 130px; left: 36px; right: 8px;
    list-style: none; font-size: 11.5px; letter-spacing: .1px; line-height: 24.5px;
    white-space: nowrap;
  }
  .services li::before {
    content: ""; display: inline-block; width: 4px; height: 4px; border-radius: 50%;
    background: var(--purple); margin-right: 12px; vertical-align: middle;
  }
  .pharmacy .photo {
    position: absolute; top: 392px; left: 0; width: 495px; height: 180px;
    background: linear-gradient(100deg, #d9b7a3 0%, #c9a28d 35%, #2f6e78 60%, #1d4e57 100%);
  }
  .pharmacy .info-band {
    position: absolute; top: 548px; left: 0; width: 495px; height: 100px;
    color: var(--white); text-align: center; white-space: nowrap;
  }
  .info-band .address { position: absolute; top: 30px; width: 100%; font-weight: 700; font-size: 16px; }
  .info-band .hours { position: absolute; top: 60px; width: 100%; font-size: 13.5px; }
  .pharmacy .contact-band {
    position: absolute; top: 648px; left: 0; width: 495px; height: 52px;
    background: var(--green);
    display: flex; align-items: center; justify-content: space-between; padding: 0 34px;
    color: var(--purple); font-weight: 700; font-size: 12.5px; letter-spacing: .4px;
    white-space: nowrap;
  }
  .contact { display: flex; align-items: center; gap: 10px; white-space: nowrap; }
  .icon-box {
    width: 22px; height: 22px; background: var(--purple); flex: none;
    display: flex; align-items: center; justify-content: center;
  }

  /* ---------- Travel side ---------- */
  .travel { left: 635px; background: var(--navy); color: var(--white); }
  .travel .brand {
    position: absolute; top: 26px; left: 22px;
    display: flex; align-items: center; gap: 8px;
    font-weight: 700; font-size: 12px; letter-spacing: .3px; color: var(--white);
  }
  .travel .brand-mark { width: 26px; height: 26px; border-radius: 50%; background: var(--white); }
  .column { position: absolute; top: 300px; }
  .column.vaccines { left: 30px; width: 220px; }
  .column.malaria { left: 262px; width: 214px; top: 286px; }
  .travel h2 {
    color: var(--sky); font-weight: 700; font-size: 18px; letter-spacing: 1px;
    text-transform: uppercase; margin-bottom: 8px; white-space: nowrap;
  }
  .travel h3 { color: var(--sky); font-weight: 600; font-size: 15px; margin: 16px 0 6px; white-space: nowrap; }
  .price-list { list-style: none; font-size: 10px; line-height: 16px; }
  .price-list li { display: flex; justify-content: space-between; gap: 6px; white-space: nowrap; }
  .price-list li span:first-child::before { content: "• "; }
  .note-list { list-style: none; font-size: 10px; line-height: 16px; }
  .note-list li { margin-bottom: 6px; }
  .note-list li::before { content: "• "; }
  .travel .notes {
    position: absolute; top: 552px; left: 12px; right: 12px; text-align: center;
  }
  .notes .lead { color: var(--sky); font-weight: 600; font-size: 10.8px; margin-bottom: 8px; white-space: nowrap; }
  .notes .fine { font-size: 10.5px; line-height: 17px; white-space: nowrap; }
  .travel .contact-band {
    position: absolute; top: 640px; left: 0; width: 495px; height: 60px;
    background: var(--sky);
    display: flex; align-items: center; justify-content: space-between; padding: 0 20px;
    color: var(--navy); font-weight: 700; font-size: 13px; letter-spacing: .3px;
  }
  .travel .icon-box { width: 28px; height: 28px; background: var(--white); }
  .travel .contact-band .phone-num { color: var(--white); font-size: 15px; }
</style>
</head>
<body>

<!-- Pharmacy services side -->
<section class="leaflet pharmacy">
  <svg class="deco" width="495" height="700" viewBox="0 0 495 700" aria-hidden="true">
    <path d="M0 0 H120 Q22 60 0 200 Z" fill="var(--purple)"/>
    <path d="M128 0 Q28 62 3 208" fill="none" stroke="var(--green)" stroke-width="4"/>
  </svg>

  <div class="brand"><span class="brand-mark"></span>Birchwell Chemist</div>

  <p class="intro">Long-established independent pharmacy offering<br>a wide range of services including:</p>

  <ul class="services">
    <li>Free prescription collection &amp; delivery service</li>
    <li>Large stocks, multiple suppliers &amp; efficient, personal service</li>
    <li>Experienced staff working with cutting edge automation</li>
    <li>Cholesterol Testing</li>
    <li>Quit Smoking Service</li>
    <li>Minor Ailments Scheme</li>
    <li>Mobility Aids</li>
    <li>Free Text Notification Service</li>
    <li>Seasonal Flu Vaccination</li>
    <li>Private vaccinations for individuals &amp; groups</li>
  </ul>

  <div class="photo" role="img" aria-label="Photograph of a vaccination being given into an upper arm"></div>

  <svg class="deco" width="495" height="700" viewBox="0 0 495 700" aria-hidden="true">
    <path d="M0 568 L495 540 L495 648 L0 648 Z" fill="var(--purple)"/>
    <path d="M430 648 Q480 610 495 540 L495 648 Z" fill="var(--green)"/>
  </svg>

  <div class="info-band">
    <p class="address">14 Market Row, Ashby Fell. FG2 4QT</p>
    <p class="hours">Monday to Friday: 8.30am – 6.00pm &amp; Saturday: 8.30am – 4.00pm</p>
  </div>

  <div class="contact-band">
    <span class="contact">
      <span class="icon-box">
        <svg width="14" height="14" viewBox="0 0 14 14" fill="none" stroke="#fff" stroke-width="1.2"><circle cx="7" cy="7" r="6"/><ellipse cx="7" cy="7" rx="2.6" ry="6"/><path d="M1 7 H13 M2 4 H12 M2 10 H12"/></svg>
      </span>www.fellgatejourneyclinic.co.uk
    </span>
    <span class="contact">
      <span class="icon-box">
        <svg width="14" height="14" viewBox="0 0 24 24" fill="#fff"><path d="M6.6 10.8a15.1 15.1 0 0 0 6.6 6.6l2.2-2.2a1 1 0 0 1 1-.25 11.4 11.4 0 0 0 3.6.57 1 1 0 0 1 1 1V20a1 1 0 0 1-1 1A17 17 0 0 1 3 4a1 1 0 0 1 1-1h3.5a1 1 0 0 1 1 1c0 1.25.2 2.45.57 3.57a1 1 0 0 1-.25 1z"/></svg>
      </span>01632 960418
    </span>
  </div>
</section>

<!-- Travel clinic side -->
<section class="leaflet travel">
  <svg class="deco" width="495" height="300" viewBox="0 0 495 300" role="img" aria-label="Photograph of a tropical beach with a palm tree, a striped hammock and turquoise sea">
    <defs>
      <linearGradient id="beach" x1="0" y1="0" x2="0" y2="1">
        <stop offset="0" stop-color="#3f8fd6"/>
        <stop offset=".35" stop-color="#9fd0ef"/>
        <stop offset=".55" stop-color="#3fb9c4"/>
        <stop offset=".8" stop-color="#e8e0cc"/>
        <stop offset="1" stop-color="#d9cdb2"/>
      </linearGradient>
    </defs>
    <path d="M60 0 H495 V150 Q380 280 200 262 Q70 248 30 160 Q20 60 60 0 Z" fill="url(#beach)"/>
    <path d="M32 168 Q80 252 200 266 Q380 284 495 156" fill="none" stroke="var(--sky)" stroke-width="8"/>
  </svg>

  <div class="brand"><span class="brand-mark"></span>Fellgate Journey Clinic</div>

  <div class="column vaccines">
    <h2>Travel Vaccines</h2>
    <ul class="price-list">
      <li><span>Cholera</span><span>£25</span></li>
      <li><span>Diphtheria Tetanus and Polio</span><span>£30</span></li>
      <li><span>Hepatitis A</span><span>£40</span></li>
      <li><span>Hepatitis B</span><span>£40</span></li>
      <li><span>Hepatitis A &amp; B (combined)</span><span>£70</span></li>
      <li><span>Hepatitis A &amp; Typhoid (combined)</span><span>£70</span></li>
      <li><span>Japanese Encephalitis</span><span>£85</span></li>
      <li><span>Meningitis ACWY</span><span>£50</span></li>
      <li><span>Rabies</span><span>£60</span></li>
      <li><span>Tick Borne Encephalitis</span><span>£60</span></li>
      <li><span>Typhoid</span><span>£35</span></li>
    </ul>
  </div>

  <div class="column malaria">
    <h2>Antimalarials</h2>
    <ul class="note-list">
      <li>Generic Malavex<br>(Atovaquone/Proguanil) - £2 per tablet</li>
      <li>Doxycycline 100mg - 50p per capsule</li>
    </ul>
    <h3>We also vaccinate against:</h3>
    <ul class="price-list">
      <li><span>Chickenpox</span><span>£60</span></li>
      <li><span>Measles Mumps &amp; Rubella (MMR)</span><span>£40</span></li>
      <li><span>Meningitis B</span><span>£110</span></li>
      <li><span>Shingles</span><span>£150</span></li>
      <li><span>Human Papilloma Virus (HPV)</span><span>£150</span></li>
    </ul>
  </div>

  <div class="notes">
    <p class="lead">*Prices are per dose &amp; more than one dose of vaccine may be needed</p>
    <p class="fine">**The availability and price of the above may vary. During shortages wholesale<br>prices can rise and we will inform you of any price changes.</p>
  </div>

  <div class="contact-band">
    <span class="contact">
      <span class="icon-box">
        <svg width="18" height="18" viewBox="0 0 14 14" fill="none" stroke="var(--sky)" stroke-width="1.2"><circle cx="7" cy="7" r="6"/><ellipse cx="7" cy="7" rx="2.6" ry="6"/><path d="M1 7 H13 M2 4 H12 M2 10 H12"/></svg>
      </span>www.fellgatejourneyclinic.co.uk
    </span>
    <span class="contact">
      <span class="icon-box">
        <svg width="18" height="18" viewBox="0 0 24 24" fill="var(--sky)"><path d="M6.6 10.8a15.1 15.1 0 0 0 6.6 6.6l2.2-2.2a1 1 0 0 1 1-.25 11.4 11.4 0 0 0 3.6.57 1 1 0 0 1 1 1V20a1 1 0 0 1-1 1A17 17 0 0 1 3 4a1 1 0 0 1 1-1h3.5a1 1 0 0 1 1 1c0 1.25.2 2.45.57 3.57a1 1 0 0 1-.25 1z"/></svg>
      </span><span class="phone-num">01632 960418</span>
    </span>
  </div>
</section>

</body>
</html>
```